Web Design Project for accounting firm

Hi winners
we are a chartered accountancy firm. We do really want to get into SEO. The link below is to our current website which I don't really like as it looks too simple.
www.qmledgerwise.com.au
In the homepage
I want to have Service tab, Testimonial tab, Events tab, Partner tab, blog tab and contact us tab
I want to have a section which have a bit description of the rencent blog and by clicking the section,you get into the real blogging page
I want a section which shows the most current client testimonials and by click into it, it gives you the testimonial page
I want a section for service which have a discription of the service overall and once click into more details, service details page pop up
I want a section for parter which had a bit description of the partner and linked to the detailed partner page
a section shows the contact number
a section for social media
a section for my logos, a section for QG logo and a section says "Liability limited by a scheme approved under Professional Standards Legislation"
In the first round, everyone can just design the homepage for me. And I will pick a couple for the second round to design the service page. and then I pick one to finish off the whole web design project.
below are the website I am planning to get
http://www.tallowmere.com.au/
http://www.brightpathledgers.com.au/ (my favourate)
Here is the link to download the QG logo
http://www.qualifiedtallyguild.com.au/Members/Marketing-your-practice/Logos
Updates
Hi Guys
I have reloaded the attachments. Hopefully works this time
I also add the link to the QG logo since someone has just asked
Will guarantee the payment when something good comes up. Won't wait until the due date.
Hi designers
I have guaranteed the payment. I am open to any good design now.
Marta

```html
<!DOCTYPE html>
<html lang="en">
<head>
<meta charset="utf-8">
<title>QM Ledgerwise Accounting — Home</title>
<link rel="stylesheet" href="https://fonts.googleapis.com/css2?family=Fauna+One&family=Arimo:wght@400;700&display=swap">
<style>
  :root {
    --tan: #d3c2a9;
    --tan-dark: #c4b094;
    --tan-accent: #c9b79c;
    --ink: #2f2f2f;
    --charcoal: #333333;
    --black: #000000;
    --light-band: #f2f2f2;
    --white: #ffffff;
    --grey-text: #a9a9a9;
    --field: #c8c8c8;
    --line: #3a3a3a;
  }
  * { box-sizing: border-box; margin: 0; padding: 0; }
  html, body { width: 1071px; height: 1200px; overflow: hidden; }
  body { position: relative; background: var(--white); font-family: "Fauna One", serif; color: var(--ink); }
  .abs { position: absolute; }

  /* Header */
  .site-header { left: 0; top: 0; width: 1071px; height: 151px; background: linear-gradient(180deg, var(--tan) 0%, var(--tan-dark) 100%); }
  .brand { left: 140px; top: 22px; display: flex; align-items: center; gap: 12px; }
  .brand-mark { width: 52px; height: 52px; background: var(--ink); }
  .brand-name { font-size: 30px; color: var(--ink); line-height: 1; margin-top: -14px; }
  .brand-tagline { left: 270px; top: 64px; font-size: 11px; color: var(--ink); }
  .social { left: 740px; top: 10px; }
  .phone { left: 762px; top: 43px; font-family: "Arimo", sans-serif; font-size: 13px; color: var(--ink); }
  .main-nav { top: 129px; font-size: 14.5px; color: var(--ink); }
  .nav-active-bar { left: 140px; top: 147px; width: 56px; height: 5px; background: var(--ink); }

  /* Hero */
  .hero-photo { left: 144px; top: 181px; width: 278px; height: 206px; background: radial-gradient(ellipse at 45% 50%, #f4f4f4 0%, #cfcfcf 70%, #bdbdbd 100%); }
  .slider-dots { left: 255px; top: 395px; }
  .welcome-title { left: 438px; top: 180px; font-size: 22px; font-weight: 400; }
  .welcome-text { left: 438px; top: 224px; width: 400px; font-size: 13px; line-height: 13.6px; }

  .btn { display: flex; align-items: center; justify-content: center; font-size: 14.5px;
         clip-path: polygon(5px 0, calc(100% - 5px) 0, 100% 5px, 100% calc(100% - 5px), calc(100% - 5px) 100%, 5px 100%, 0 calc(100% - 5px), 0 5px); }
  .btn-dark { background: var(--ink); color: var(--white); }
  .btn-tan { background: var(--tan-accent); color: var(--ink); }

  .section-title { display: flex; align-items: center; gap: 6px; font-size: 22px; font-weight: 400; }
  .section-title::before { content: ""; width: 12px; height: 12px; background: var(--tan-accent); border-radius: 2px; }
  .on-dark { color: var(--white); }

  /* Services */
  .service { width: 170px; text-align: center; top: 450px; }
  .service-label { font-size: 12px; margin-top: 6px; white-space: nowrap; }

  /* Partners & blog band */
  .light-band { left: 0; top: 620px; width: 1071px; height: 259px; background: var(--light-band); }
  .blog-title { left: 566px; top: 620px; display: flex; align-items: center; gap: 8px; font-size: 22px; }
  .blog-title::before { content: ""; width: 12px; height: 12px; background: var(--tan-accent); border-radius: 2px; margin-right: 6px; }
  .blog-title .sub { font-size: 15px; }
  .blog-list { left: 566px; top: 660px; width: 291px; list-style: none; font-family: "Arimo", sans-serif; font-size: 11px; color: var(--ink); }
  .blog-list li { display: flex; align-items: center; gap: 9px; height: 32px; border-bottom: 1.5px solid var(--line); padding-top: 3px; white-space: nowrap; }
  .blog-list li::before { content: ""; width: 12px; height: 12px; background: var(--line); border-radius: 2px; }

  /* Dark band */
  .dark-band { left: 0; top: 879px; width: 1071px; height: 256px; background: var(--charcoal); }
  .testimonial-text { left: 139px; top: 924px; width: 390px; font-size: 11.5px; line-height: 13px; color: var(--grey-text); }
  .testimonial-author { left: 380px; top: 1000px; width: 139px; text-align: right; font-size: 13px; color: var(--white); }
  .guild { left: 137px; top: 1063px; display: flex; align-items: center; gap: 10px; }
  .guild-circle { width: 60px; height: 60px; border-radius: 50%; background: var(--black); }
  .guild-name { font-size: 15px; line-height: 17px; color: #5a5a5a; width: 100px; }
  .liability { left: 328px; top: 1077px; width: 190px; font-family: "Arimo", sans-serif; font-size: 8.8px; line-height: 10px; color: var(--white); }
  .field { left: 569px; width: 288px; background: var(--field); color: var(--white); font-family: "Arimo", sans-serif; font-weight: 700; font-size: 11px; padding: 5px 8px; }

  /* Footer */
  .site-footer { left: 0; top: 1135px; width: 1071px; height: 65px; background: var(--black); }
  .newsletter-label { left: 137px; top: 1147px; font-family: "Arimo", sans-serif; font-weight: 700; font-size: 12px; color: var(--white); }
  .newsletter-input { left: 219px; top: 1141px; width: 139px; height: 25px; border-radius: 5px; background: #a6a6a6; }
  .footer-nav { top: 1146px; font-family: "Arimo", sans-serif; font-size: 11.5px; color: var(--white); }
  .footer-sep { top: 1144px; width: 1.5px; height: 20px; background: var(--white); }
  .rights { left: 750px; top: 1168px; width: 112px; text-align: right; font-family: "Arimo", sans-serif; font-size: 11px; color: var(--white); }
</style>
</head>
<body>

<header class="abs site-header"></header>
<div class="abs brand"><span class="brand-mark"></span><span class="brand-name">QM Ledgerwise</span></div>
<div class="abs brand-tagline">Chartered Accountants &amp; Registered Tax Agent</div>
<svg class="abs social" width="90" height="30" viewBox="0 0 90 30" aria-label="Social media links">
  <circle cx="12" cy="13" r="12" fill="#2f2f2f"/>
  <circle cx="39" cy="13" r="12" fill="#2f2f2f"/>
  <circle cx="68" cy="13" r="12" fill="#2f2f2f"/>
</svg>
<div class="abs phone">(02) 5550 1829</div>

<nav>
  <span class="abs main-nav" style="left:147px">Home</span>
  <span class="abs main-nav" style="left:240px">Services</span>
  <span class="abs main-nav" style="left:343px">Testimonials</span>
  <span class="abs main-nav" style="left:481px">Events</span>
  <span class="abs main-nav" style="left:581px">Partners</span>
  <span class="abs main-nav" style="left:695px">Blog</span>
  <span class="abs main-nav" style="left:772px">Contact Us</span>
</nav>
<div class="abs nav-active-bar"></div>

<div class="abs hero-photo" role="img" aria-label="Photo of a smiling accountant holding a document folder"></div>
<svg class="abs slider-dots" width="64" height="12" viewBox="0 0 64 12" aria-label="Slide indicators">
  <circle cx="6" cy="6" r="4" fill="none" stroke="#2f2f2f" stroke-width="1.3"/>
  <circle cx="22" cy="6" r="4" fill="none" stroke="#2f2f2f" stroke-width="1.3"/>
  <circle cx="38" cy="6" r="4" fill="none" stroke="#2f2f2f" stroke-width="1.3"/>
  <circle cx="55" cy="6" r="4" fill="none" stroke="#2f2f2f" stroke-width="1.3"/>
</svg>
<h1 class="abs welcome-title">Welcome to QM Ledgerwise Accounting</h1>
<p class="abs welcome-text">QM Ledgerwise Accounting is a registered tax agent and Chartered Accountant based in Harbourvale and Westmere Sydney. With years of experience in tax, accounting and audit, we have been providing individuals and businesses a comprehensive range of tax and accounting services that are tailored to clients' needs and will benefit them at the most. For any inquiries, email us on info@qmledgerwise.com.au</p>
<div class="abs btn btn-dark" style="left:437px;top:364px;width:90px;height:29px">Learn more</div>

<h2 class="abs section-title" style="left:143px;top:414px">Featured Services</h2>

<svg width="0" height="0" style="position:absolute">
  <defs>
    <radialGradient id="disc" cx="40%" cy="35%" r="70%">
      <stop offset="0" stop-color="#bdbdbd"/>
      <stop offset="0.7" stop-color="#8d8d8d"/>
      <stop offset="1" stop-color="#6e6e6e"/>
    </radialGradient>
  </defs>
</svg>

<div class="abs service" style="left:102px">
  <svg width="124" height="124" viewBox="0 0 124 124" aria-label="Calculator icon">
    <circle cx="62" cy="62" r="60" fill="#f4f4f4" stroke="#dcdcdc" stroke-width="2"/>
    <circle cx="62" cy="60" r="47" fill="url(#disc)"/>
    <rect x="45" y="36" width="34" height="46" rx="5" fill="none" stroke="#fff" stroke-width="3"/>
    <rect x="51" y="42" width="22" height="9" fill="#fff"/>
    <g fill="#fff"><circle cx="54" cy="59" r="2.5"/><circle cx="62" cy="59" r="2.5"/><circle cx="70" cy="59" r="2.5"/><circle cx="54" cy="67" r="2.5"/><circle cx="62" cy="67" r="2.5"/><circle cx="70" cy="67" r="2.5"/><circle cx="54" cy="75" r="2.5"/><circle cx="62" cy="75" r="2.5"/><circle cx="70" cy="75" r="2.5"/></g>
  </svg>
  <div class="service-label">Audit &amp; Assurance</div>
</div>
<div class="abs service" style="left:255px">
  <svg width="124" height="124" viewBox="0 0 124 124" aria-label="Magnifier icon">
    <circle cx="62" cy="62" r="60" fill="#f4f4f4" stroke="#dcdcdc" stroke-width="2"/>
    <circle cx="62" cy="60" r="47" fill="url(#disc)"/>
    <circle cx="67" cy="54" r="15" fill="none" stroke="#fff" stroke-width="4"/>
    <path d="M67 46v16M59 54h16" stroke="#fff" stroke-width="3"/>
    <path d="M56 65L42 79" stroke="#fff" stroke-width="6" stroke-linecap="round"/>
  </svg>
  <div class="service-label">Migration Audit</div>
</div>
<div class="abs service" style="left:404px">
  <svg width="124" height="124" viewBox="0 0 124 124" aria-label="Savings icon">
    <circle cx="62" cy="62" r="60" fill="#f4f4f4" stroke="#dcdcdc" stroke-width="2"/>
    <circle cx="62" cy="60" r="47" fill="url(#disc)"/>
    <ellipse cx="62" cy="62" rx="21" ry="15" fill="none" stroke="#fff" stroke-width="3"/>
    <path d="M55 47h10" stroke="#fff" stroke-width="3"/>
    <path d="M52 76v5M72 76v5" stroke="#fff" stroke-width="3"/>
    <circle cx="75" cy="58" r="2" fill="#fff"/>
  </svg>
  <div class="service-label">Superannuation</div>
</div>
<div class="abs service" style="left:562px">
  <svg width="124" height="124" viewBox="0 0 124 124" aria-label="Gavel icon">
    <circle cx="62" cy="62" r="60" fill="#f4f4f4" stroke="#dcdcdc" stroke-width="2"/>
    <circle cx="62" cy="60" r="47" fill="url(#disc)"/>
    <rect x="50" y="36" width="24" height="12" rx="2" fill="none" stroke="#fff" stroke-width="3" transform="rotate(-30 62 42)"/>
    <path d="M64 46L76 68" stroke="#fff" stroke-width="4"/>
    <rect x="46" y="74" width="28" height="7" fill="none" stroke="#fff" stroke-width="3"/>
    <rect x="42" y="81" width="36" height="5" fill="#fff"/>
  </svg>
  <div class="service-label">Tax &amp; Accounting</div>
</div>
<div class="abs service" style="left:718px">
  <svg width="124" height="124" viewBox="0 0 124 124" aria-label="Scissors icon">
    <circle cx="62" cy="62" r="60" fill="#f4f4f4" stroke="#dcdcdc" stroke-width="2"/>
    <circle cx="62" cy="60" r="47" fill="url(#disc)"/>
    <rect x="60" y="40" width="24" height="30" fill="none" stroke="#fff" stroke-width="2.5" transform="rotate(20 72 55)"/>
    <circle cx="46" cy="52" r="5" fill="none" stroke="#fff" stroke-width="3"/>
    <circle cx="46" cy="68" r="5" fill="none" stroke="#fff" stroke-width="3"/>
    <path d="M50 55L72 66M50 65L72 52" stroke="#fff" stroke-width="3"/>
  </svg>
  <div class="service-label">Management consulting</div>
</div>

<section class="abs light-band"></section>
<h2 class="abs section-title" style="left:139px;top:621px">Partners</h2>
<svg class="abs" style="left:130px;top:654px" width="310" height="204" viewBox="0 0 310 204" aria-label="Partner badges">
  <circle cx="40" cy="44" r="36" fill="#9b9b9b"/>
  <rect x="125" y="4" width="73" height="86" rx="6" fill="#6f6f6f"/>
  <rect x="237" y="10" width="62" height="70" fill="#8a8a8a"/>
  <rect x="4" y="106" width="84" height="84" rx="4" fill="#8a8a8a"/>
  <circle cx="162" cy="150" r="48" fill="#a9a9a9"/>
  <rect x="242" y="106" width="52" height="83" rx="4" fill="#9b9b9b"/>
</svg>

<div class="abs blog-title">Blog <span>|</span> <span class="sub">latest News</span></div>
<ul class="abs blog-list">
  <li>From 1 July 2012, small businesses that accou...</li>
  <li>From 1 July 2012, small businesses that accou...</li>
  <li>From 1 July 2012, small businesses that accou...</li>
  <li>From 1 July 2012, small businesses that accou...</li>
  <li>From 1 July 2012, small businesses that accou...</li>
</ul>
<div class="abs btn btn-dark" style="left:771px;top:840px;width:91px;height:30px">Learn more</div>

<section class="abs dark-band"></section>
<h2 class="abs section-title on-dark" style="left:139px;top:889px">Testimonials</h2>
<p class="abs testimonial-text">The representative I spoke with verified my info and said he would call me back once he looked into the problem. Sure enough he called back within 10 minutes and pointed the problem out to me. Once i made the change the problem has been solved. Thank to you 2007 will be a cheaper and more productive year for us at our company</p>
<div class="abs testimonial-author">Dana Whitcombe</div>
<div class="abs btn btn-tan" style="left:141px;top:1020px;width:90px;height:32px">Learn more</div>
<div class="abs guild"><span class="guild-circle"></span><span class="guild-name">Qualified Tally Guild</span></div>
<p class="abs liability">Liability limited by a scheme approved under Professional Standards Legislation</p>

<h2 class="abs section-title on-dark" style="left:565px;top:889px">Contact Us</h2>
<div class="abs field" style="top:924px;height:26px">Email</div>
<div class="abs field" style="top:959px;height:26px">Tel</div>
<div class="abs field" style="top:994px;height:26px">Subject</div>
<div class="abs field" style="top:1029px;height:93px">Contect</div>

<footer class="abs site-footer"></footer>
<div class="abs newsletter-label">newsletter :</div>
<div class="abs newsletter-input"></div>
<span class="abs footer-nav" style="left:388px">Home</span>
<span class="abs footer-sep" style="left:431px"></span>
<span class="abs footer-nav" style="left:447px">Services</span>
<span class="abs footer-sep" style="left:505px"></span>
<span class="abs footer-nav" style="left:522px">Testimonials</span>
<span class="abs footer-sep" style="left:598px"></span>
<span class="abs footer-nav" style="left:615px">Events</span>
<span class="abs footer-sep" style="left:662px"></span>
<span class="abs footer-nav" style="left:674px">Partners</span>
<span class="abs footer-sep" style="left:723px"></span>
<span class="abs footer-nav" style="left:749px">Blog</span>
<span class="abs footer-sep" style="left:786px"></span>
<span class="abs footer-nav" style="left:804px">Contact Us</span>
<div class="abs rights">all rights reserved</div>

</body>
</html>
```